Criação de Kit com 6 Layouts de Post para Redes Sociais (Facebook, Instagram e etc) + Capa de Facebook para Imóveis
A empresa queria:
" GESTÃO E CONSULTORIA DE INVESTIMENTOS LASTREADOS EM IMÓVEIS "

```html
<!DOCTYPE html>
<html lang="pt-BR">
<head>
<meta charset="UTF-8">
<title>Alavancagem Patrimonial – Novaterra Imóveis</title>
<link href="https://fonts.googleapis.com/css2?family=Montserrat:wght@500;600;700&display=swap" rel="stylesheet">
<style>
  :root{
    --navy:#1d4a6e;
    --blue:#1f5fa8;
    --teal:#27b8a8;
    --teal-light:#3fd0c0;
    --white:#ffffff;
    --paper:#f7f9fb;
  }
  html,body{margin:0;padding:0;overflow:hidden;}
  .post{
    position:relative;width:1200px;height:1200px;overflow:hidden;
    background:var(--paper);
    font-family:"Montserrat",sans-serif;color:var(--navy);
  }
  .property-photo{
    position:absolute;top:0;right:0;width:640px;height:1200px;
    background:linear-gradient(180deg,#eef2f5 0%,#b9c6d3 25%,#8596aa 50%,#7d8a80 72%,#6f9a55 100%);
    -webkit-mask-image:linear-gradient(90deg,transparent 0%,#000 35%);
            mask-image:linear-gradient(90deg,transparent 0%,#000 35%);
  }
  .brand{
    position:absolute;left:96px;top:190px;display:flex;align-items:center;gap:20px;
  }
  .brand-mark{width:110px;height:110px;border-radius:50%;background:linear-gradient(135deg,var(--blue),var(--teal));}
  .brand-name{font-weight:600;font-size:36px;letter-spacing:1px;color:var(--navy);}
  .headline{
    position:absolute;left:100px;top:340px;margin:0;
    font-weight:700;font-size:72px;line-height:1.12;color:var(--navy);
  }
  .subhead{
    position:absolute;left:100px;top:558px;margin:0;
    font-weight:600;font-size:52px;line-height:68px;color:var(--navy);
  }
  .cta{
    position:absolute;left:91px;top:808px;width:410px;height:72px;
    border-radius:36px;background:var(--navy);color:var(--white);
    display:flex;align-items:center;justify-content:center;
    font-weight:500;font-size:36px;
  }
  .cursor{position:absolute;left:292px;top:864px;width:46px;height:58px;}
  .wave{position:absolute;left:0;top:0;width:1200px;height:1200px;pointer-events:none;}
  .contact{
    position:absolute;left:96px;top:1078px;width:348px;height:50px;box-sizing:border-box;
    border:3px solid var(--white);border-radius:25px;
    display:flex;align-items:center;justify-content:center;gap:12px;
    color:var(--white);font-weight:500;font-size:26px;
  }
  .contact svg{width:26px;height:26px;}
</style>
</head>
<body>
<main class="post">
  <div class="property-photo" role="img" aria-label="Foto de uma casa moderna de dois andares com varanda e gramado verde à frente"></div>

  <svg class="wave" viewBox="0 0 1200 1200" aria-hidden="true">
    <defs>
      <linearGradient id="waveTeal" x1="0" y1="0" x2="1" y2="0">
        <stop offset="0" stop-color="#27b8a8"/>
        <stop offset="1" stop-color="#3fd0c0"/>
      </linearGradient>
      <linearGradient id="waveBlue" x1="0" y1="0" x2="1" y2="0">
        <stop offset="0" stop-color="#1f5fa8"/>
        <stop offset="1" stop-color="#27b8a8"/>
      </linearGradient>
    </defs>
    <path d="M0,990 C220,950 450,1010 660,1200 L0,1200 Z" fill="url(#waveTeal)"/>
    <path d="M0,1040 C230,1000 440,1070 610,1200 L0,1200 Z" fill="url(#waveBlue)"/>
  </svg>

  <div class="brand">
    <span class="brand-mark"></span>
    <span class="brand-name">NOVATERRA IMÓVEIS</span>
  </div>

  <h1 class="headline">Alavancagem<br>Patrimonial</h1>
  <p class="subhead">O imóvel<br>trabalhando<br>para você!</p>

  <div class="cta">vamos começar?</div>
  <svg class="cursor" viewBox="0 0 60 72" aria-hidden="true">
    <path d="M8,4 L8,56 L22,44 L32,66 L42,61 L32,40 L50,40 Z" fill="#ffffff" stroke="#1d4a6e" stroke-width="4" stroke-linejoin="round"/>
  </svg>

  <div class="contact">
    <svg viewBox="0 0 24 24" aria-hidden="true"><path d="M6.6 10.8a15.1 15.1 0 0 0 6.6 6.6l2.2-2.2a1 1 0 0 1 1-.25 11.4 11.4 0 0 0 3.6.57 1 1 0 0 1 1 1V20a1 1 0 0 1-1 1A17 17 0 0 1 3 4a1 1 0 0 1 1-1h3.5a1 1 0 0 1 1 1c0 1.25.2 2.45.57 3.57a1 1 0 0 1-.25 1z" fill="#ffffff"/></svg>
    <span>(00) 0 0000.0000</span>
  </div>
</main>
</body>
</html>
```